Urine collection cup with and without sterile seal sticker

Hello. We need a urine cup label designed please with

Name:
Date of Birth:
Date:
Time:
Temp℃:
Specimen ID:

Product code: TUB-47
Volume markings (e.g., 30 mL, 60 mL, 90 mL).
Vela Drug Tests logo

Could you please provide one version with the additional sterile sticker extending to the top, and one version without the additional sterile sticker?

```html
<!DOCTYPE html>
<html lang="en">
<head>
<meta charset="utf-8">
<title>Vela Drug Tests – Specimen Cup Labels</title>
<link href="https://fonts.googleapis.com/css2?family=Montserrat:wght@400;500;700&display=swap" rel="stylesheet">
<style>
  :root {
    --brand: #27a1e4;
    --backdrop: #b3b3b3;
    --ink: #111111;
    --paper: #ffffff;
    --caption: #ececec;
  }
  * { margin: 0; padding: 0; box-sizing: border-box; }
  html, body { width: 1200px; height: 3240px; overflow: hidden; }
  body { font-family: "Montserrat", Arial, sans-serif; background: var(--paper); position: relative; }

  .sheet { position: absolute; left: 0; top: 0; width: 1200px; height: 2476px; background: var(--backdrop); }

  .swatch { position: absolute; left: 886px; top: 153px; width: 130px; height: 130px; border-radius: 50%; background: var(--brand); }
  .swatch-caption { position: absolute; left: 801px; top: 330px; width: 300px; text-align: center; color: var(--caption); font-size: 35px; line-height: 55px; font-weight: 400; }

  .label { position: absolute; left: 153px; width: 887px; height: 897px; }
  .label--nonsterile { top: 330px; }
  .label--sterile { top: 1341px; }

  .label__strip { position: absolute; left: 0; top: 0; width: 111px; height: 897px; }

  .label__card { position: absolute; left: 111px; top: 249px; width: 776px; height: 648px; background: var(--paper); border-radius: 0 30px 30px 0; padding: 38px 46px 0 44px; color: var(--ink); }

  .field { display: flex; align-items: flex-end; font-size: 35px; height: 55px; font-weight: 500; }
  .field__label { white-space: nowrap; }
  .field__line { flex: 1; border-bottom: 2.5px solid var(--ink); margin: 0 0 14px 10px; }

  .product { margin-top: 54px; font-size: 35px; font-weight: 500; line-height: 55px; }
  .volume { display: flex; align-items: center; font-size: 35px; font-weight: 500; height: 55px; }
  .volume__title { margin-right: 30px; }
  .volume__option { display: flex; align-items: center; margin-right: 12px; }
  .volume__box { width: 36px; height: 36px; border: 2.5px solid var(--ink); border-radius: 7px; margin-right: 4px; }

  .brandmark { display: flex; align-items: center; margin-top: 22px; color: var(--brand); font-size: 44px; font-weight: 700; letter-spacing: -0.5px; }
  .brandmark__dot { width: 46px; height: 46px; border-radius: 50%; background: var(--brand); margin-right: 14px; }

  .scene-photo { position: absolute; left: 0; top: 2476px; width: 1200px; height: 764px; background: radial-gradient(ellipse at 50% 45%, #e3f2fb 0%, #f4f9fc 45%, #ffffff 75%); }
</style>
</head>
<body>
  <section class="sheet">
    <div class="swatch"></div>
    <p class="swatch-caption">Brand Color<br>#27a1e4</p>

    <article class="label label--nonsterile">
      <svg class="label__strip" viewBox="0 0 111 897" aria-hidden="false">
        <path d="M0,897 L0,55.5 A55.5,55.5 0 0 1 111,55.5 L111,897 Z" fill="var(--brand)"/>
        <path d="M0,232 C0,290 92,262 92,322 L92,897 L0,897 Z" fill="var(--paper)"/>
        <g fill="var(--paper)" font-family="Montserrat, Arial, sans-serif" font-weight="700" font-size="19" letter-spacing="1">
          <text transform="translate(32,259) rotate(-90)">INTERIOR</text>
          <text transform="translate(60,259) rotate(-90)">AS LONG AS SEAL</text>
          <text transform="translate(88,259) rotate(-90)">REAMAINS INTACT</text>
        </g>
        <text transform="translate(66,591) rotate(-90)" text-anchor="middle" fill="var(--brand)" font-family="Montserrat, Arial, sans-serif" font-weight="700" font-size="48" textLength="485" lengthAdjust="spacing">NONSTERILE</text>
      </svg>
      <div class="label__card">
        <div class="field"><span class="field__label">Name:</span><span class="field__line"></span></div>
        <div class="field"><span class="field__label">Date of Birth:</span><span class="field__line"></span></div>
        <div class="field"><span class="field__label">Date:</span><span class="field__line"></span></div>
        <div class="field"><span class="field__label">Time:</span><span class="field__line"></span></div>
        <div class="field"><span class="field__label">Temp:</span><span class="field__line"></span></div>
        <div class="field"><span class="field__label">Specimen ID:</span><span class="field__line"></span></div>
        <p class="product">Product code: TUB-47</p>
        <div class="volume">
          <span class="volume__title">Volume:</span>
          <span class="volume__option"><span class="volume__box"></span>30 mL</span>
          <span class="volume__option"><span class="volume__box"></span>60 mL</span>
          <span class="volume__option"><span class="volume__box"></span>90 mL</span>
        </div>
        <div class="brandmark"><span class="brandmark__dot"></span>Vela Drug Tests</div>
      </div>
    </article>

    <article class="label label--sterile">
      <svg class="label__strip" viewBox="0 0 111 897">
        <path d="M0,897 L0,55.5 A55.5,55.5 0 0 1 111,55.5 L111,897 Z" fill="var(--brand)"/>
        <path d="M0,232 C0,290 92,262 92,322 L92,897 L0,897 Z" fill="var(--paper)"/>
        <g fill="var(--paper)" font-family="Montserrat, Arial, sans-serif" font-weight="700" font-size="19" letter-spacing="1">
          <text transform="translate(32,259) rotate(-90)">INTERIOR</text>
          <text transform="translate(60,259) rotate(-90)">AS LONG AS SEAL</text>
          <text transform="translate(88,259) rotate(-90)">REAMAINS INTACT</text>
        </g>
        <text transform="translate(66,600) rotate(-90)" text-anchor="middle" fill="var(--brand)" font-family="Montserrat, Arial, sans-serif" font-weight="700" font-size="48" textLength="472" lengthAdjust="spacing">STERILE</text>
      </svg>
      <div class="label__card">
        <div class="field"><span class="field__label">Name:</span><span class="field__line"></span></div>
        <div class="field"><span class="field__label">Date of Birth:</span><span class="field__line"></span></div>
        <div class="field"><span class="field__label">Date:</span><span class="field__line"></span></div>
        <div class="field"><span class="field__label">Time:</span><span class="field__line"></span></div>
        <div class="field"><span class="field__label">Temp:</span><span class="field__line"></span></div>
        <div class="field"><span class="field__label">Specimen ID:</span><span class="field__line"></span></div>
        <p class="product">Product code: TUB-47</p>
        <div class="volume">
          <span class="volume__title">Volume:</span>
          <span class="volume__option"><span class="volume__box"></span>30 mL</span>
          <span class="volume__option"><span class="volume__box"></span>60 mL</span>
          <span class="volume__option"><span class="volume__box"></span>90 mL</span>
        </div>
        <div class="brandmark"><span class="brandmark__dot"></span>Vela Drug Tests</div>
      </div>
    </article>
  </section>

  <div class="scene-photo" role="img" aria-label="Product photo of two clear specimen cups with blue lids and yellow seals, front view showing the sterile label and back view"></div>
</body>
</html>
```